Seven nights at the harbour

Creation of the cover for the book: "Sept nuits sur le quai du port" with the joined photo of a 70 years old lady.
Title: "Seven nights along the old harbour"
Author: "Mireille Vaston"
Publisher: "Editions Morvane" (should be at the bottom of the page)
Format: 14 x 20.5 cm
The story: A senior lady (70 years old), divorced, with a beautiful face, still wants to seduce, even young men.
We found the perfect photo for the woman. We would like to ask you to make a modern cover from it.
Besoin de quelques jours pour choisir un design
Target Market(s)
Novels reader (adults)
Industry/Entity Type
book

```html
<!DOCTYPE html>
<html lang="fr">
<head>
<meta charset="utf-8">
<title>Sept nuits sur le quai du port — couverture</title>
<link rel="stylesheet" href="https://fonts.googleapis.com/css2?family=Great+Vibes&family=Cinzel:wght@400&family=Tinos:wght@400&family=Cormorant+Garamond:wght@500&display=swap">
<style>
  :root {
    --slate: #55625f;
    --slate-deep: #4c5956;
    --silver-mid: #9fa5a3;
    --silver-light: #d6d7d5;
    --silver-bright: #e6e6e4;
    --skin-hint: #c9a799;
    --ink-white: #ffffff;
    --ink-dark: #1c1c1c;
  }
  html, body {
    margin: 0;
    padding: 0;
    width: 1200px;
    height: 830px;
    overflow: hidden;
    background: var(--slate);
  }
  .cover {
    position: relative;
    width: 1200px;
    height: 830px;
    overflow: hidden;
  }
  .cover-photo {
    position: absolute;
    inset: 0;
    background:
      radial-gradient(ellipse 160px 200px at 820px 300px, rgba(201,167,153,0.55), rgba(201,167,153,0) 100%),
      radial-gradient(ellipse 520px 420px at 820px 360px, var(--silver-bright), rgba(230,230,228,0) 100%),
      linear-gradient(90deg, var(--slate-deep) 0%, var(--slate) 30%, var(--silver-mid) 48%, var(--silver-light) 70%, var(--silver-bright) 100%);
  }

  /* Back cover */
  .back-title {
    position: absolute;
    left: 70px;
    top: 86px;
    width: 418px;
    text-align: center;
    color: var(--ink-white);
  }
  .back-title .script {
    display: block;
    font-family: "Great Vibes", cursive;
    font-size: 40px;
    line-height: 44px;
  }
  .back-title .joiner {
    display: block;
    font-family: "Great Vibes", cursive;
    font-size: 18px;
    line-height: 14px;
  }
  .back-title .caps {
    display: block;
    font-family: "Cormorant Garamond", serif;
    font-weight: 500;
    font-size: 40px;
    line-height: 40px;
    letter-spacing: 1px;
  }
  .blurb {
    position: absolute;
    left: 70px;
    top: 213px;
    width: 418px;
    margin: 0;
    font-family: "Tinos", serif;
    font-size: 12.8px;
    line-height: 17px;
    color: var(--ink-white);
    text-align: justify;
    text-align-last: center;
    hyphens: auto;
  }
  .barcode-space {
    position: absolute;
    left: 70px;
    top: 698px;
    width: 124px;
    height: 83px;
    background: var(--ink-white);
  }
  .publisher-back {
    position: absolute;
    left: 214px;
    top: 760px;
    font-family: "Tinos", serif;
    font-size: 19px;
    color: var(--ink-white);
    letter-spacing: 0.5px;
  }

  /* Spine */
  .spine-line {
    position: absolute;
    left: 606px;
    top: 395px;
    width: 740px;
    transform: translate(-50%, -50%) rotate(-90deg);
    white-space: nowrap;
    color: var(--ink-white);
    display: flex;
    align-items: baseline;
    gap: 16px;
  }
  .spine-author {
    font-family: "Cinzel", serif;
    font-size: 15px;
    letter-spacing: 7px;
    color: var(--ink-dark);
  }
  .spine-title-script {
    font-family: "Great Vibes", cursive;
    font-size: 28px;
  }
  .spine-title-small {
    font-family: "Great Vibes", cursive;
    font-size: 15px;
  }
  .spine-title-caps {
    font-family: "Cormorant Garamond", serif;
    font-weight: 500;
    font-size: 22px;
  }
  .spine-mark {
    position: absolute;
    left: 580px;
    top: 758px;
    width: 52px;
    height: 52px;
  }

  /* Front cover */
  .front-author {
    position: absolute;
    left: 700px;
    top: 36px;
    width: 420px;
    font-family: "Cinzel", serif;
    font-size: 26px;
    letter-spacing: 9px;
    color: var(--ink-dark);
    white-space: nowrap;
  }
  .front-title {
    position: absolute;
    left: 700px;
    top: 440px;
    width: 460px;
    text-align: center;
    color: var(--ink-white);
    text-shadow: 0 3px 8px rgba(0,0,0,0.35);
  }
  .front-title .script {
    display: block;
    font-family: "Great Vibes", cursive;
    font-size: 86px;
    line-height: 82px;
  }
  .front-title .joiner {
    display: block;
    font-family: "Great Vibes", cursive;
    font-size: 38px;
    line-height: 34px;
  }
  .front-title .caps {
    display: block;
    font-family: "Cormorant Garamond", serif;
    font-weight: 500;
    font-size: 112px;
    line-height: 96px;
    letter-spacing: 2px;
  }
  .publisher-front {
    position: absolute;
    left: 700px;
    top: 780px;
    width: 460px;
    text-align: center;
    font-family: "Tinos", serif;
    font-size: 19px;
    color: var(--ink-white);
    letter-spacing: 0.5px;
  }
</style>
</head>
<body>
  <main class="cover">
    <div class="cover-photo" role="img" aria-label="Portrait photograph of a 70-year-old woman with long windswept silver hair across her face, set against a slate grey backdrop"></div>

    <section class="back-cover">
      <h2 class="back-title">
        <span class="script">Sept nuits sur le quai</span>
        <span class="joiner">du</span>
        <span class="caps">PORT</span>
      </h2>
      <p class="blurb">Lorem ipsum dolor sit amet, consectetur adipiscing elit. Etiam nisi diam, convallis at dictum in, dapibus sit amet mi. Praesent rutrum lacus magna, eget molestie velit lobortis non. Etiam sollicitudin tristique massa at sodales. Duis faucibus egestas odio pretium facilisis. Etiam scelerisque in mauris sed interdum. Nullam diam turpis, sodales ut feugiat in, suscipit in erat. Nullam et risus egestas, porta elit vel, semper lacus. Cras pretium consequat vestibulum. In id sapien ut ex blandit suscipit a sit amet mauris. Ut pharetra gravida tempus. Sed ornare quam sed quam convallis, bibendum pulvinar magna sollicitudin. Duis vel tempor enim. Nulla sit amet urna ac ex pretium ullamcorper.</p>
      <div class="barcode-space"></div>
      <div class="publisher-back">EDITIONS MORVANE</div>
    </section>

    <section class="spine">
      <div class="spine-line">
        <span class="spine-author">MIREILLE VASTON</span>
        <span class="spine-title-script">Sept nuits sur le quai</span>
        <span class="spine-title-small">du</span>
        <span class="spine-title-caps">PORT</span>
      </div>
      <svg class="spine-mark" viewBox="0 0 52 52" aria-hidden="true">
        <circle cx="26" cy="26" r="25" fill="#ffffff" stroke="#9a9a9a" stroke-width="1"/>
      </svg>
    </section>

    <section class="front-cover">
      <div class="front-author">MIREILLE VASTON</div>
      <h1 class="front-title">
        <span class="script">Sept nuits</span>
        <span class="script">sur le quai</span>
        <span class="joiner">du</span>
        <span class="caps">PORT</span>
      </h1>
      <div class="publisher-front">EDITIONS MORVANE</div>
    </section>
  </main>
</body>
</html>
```